Maputo Partial Urbanization Plan (PPU) Project Needs a Web Design

We need a web design for a new project. The Corvane Fund and the Municipality of Velstrand has awarded Brixel a contract valued at US $1.1 million to provide consulting services for the design of the Partial Urbanization Plan (PUP) of the "Baixa", or central business district, of the historic capital of Mozambique - Maputo. The primary goal of the project website is to foster public engagement: generate public awareness and interest in the project, solicit public input and feedback, and encourage involvement and action related to the project.
We would like to see designs that mirror the colors of the city of Maputo flag (light green and dark green with yellow accents). The final design should be interactive and should communicate urban planning, development, and civic engagement.
We would like to use a simple, open source platform that will allow us to easily make text and image updates. We will not have an in-house web developer helping to manage the site, thus we need an easy way to access the content management system "back-end" or make simple updates.
Target Market(s)
Primary audience: citizens of Maputo. Secondary audiences: project staff, contractor staff, client staff, wider development community.
Industry/Entity Type
Business
Requirements
Must have
- The website should have the following pages:
Homepage (landing page)
About (Vision/why)
Data
Events (public engagements)
Blog
Contact Us
Stakeholder Portal
Nice to have
- The Homepage could use flash to slide through 3-4 photos automatically. The homepage would ideally have a top bar or side bar linking to the other webpages, with a road map at the bottom.
Space to put photos and text on each webpage.
The Events page could have a calendar to show when specific events are taking place.

```html
<!DOCTYPE html>
<html lang="en">
<head>
<meta charset="utf-8">
<title>Velstrand Partial Urbanization Plan</title>
<link href="https://fonts.googleapis.com/css2?family=Arimo:wght@400;700&display=swap" rel="stylesheet">
<style>
:root{
  --page:#e6f2c5;
  --head-top:#93c21f;
  --head-bottom:#3b7706;
  --tab:#8fbb2c;
  --tab-light:#a9cf4a;
  --accent:#8db52c;
  --accent-dark:#6f9a1a;
  --rule:#b9d47a;
  --text:#444a3c;
  --heading:#3b3f35;
  --footer:#3f7b0b;
  --white:#ffffff;
}
*{margin:0;padding:0;box-sizing:border-box}
html,body{width:1200px;height:1000px;overflow:hidden}
body{position:relative;background:var(--page);font-family:"Arimo",Arial,sans-serif;color:var(--text)}
.abs{position:absolute}

.site-header{left:0;top:0;width:1200px;height:111px;background:linear-gradient(var(--head-top),var(--head-bottom))}
.brand{left:216px;top:30px;display:flex;align-items:center;gap:10px;color:var(--white);font-size:24px;font-weight:700}
.brand-mark{width:34px;height:34px;border-radius:50%;background:#f2c81c}
.header-email{left:860px;top:38px;width:143px;text-align:right;color:var(--white);font-size:12px}
.main-nav{left:559px;top:81px;height:30px;display:flex}
.main-nav a{display:block;height:30px;margin-right:3px;background:linear-gradient(var(--tab-light),var(--tab));border-radius:5px 5px 0 0;color:var(--white);font-size:11px;text-decoration:none;text-align:center;line-height:31px}
.main-nav a.current{color:#1f2a10}

.slider{left:208px;top:121px;width:796px;height:300px;background:var(--white);border-radius:7px;padding:5px 6px}
.slide-photo{width:784px;height:290px;background:linear-gradient(90deg,#4b5f9c 0%,#3e5a8a 30%,#4f7c8e 42%,#5e7f52 60%,#3d4a4a 72%,#2b2622 100%)}
.slide-arrow{width:40px;height:40px;border-radius:50%;background:rgba(255,255,255,.35)}
.slide-arrow svg{display:block}
.slide-dot{width:14px;height:14px;border-radius:50%;background:var(--accent)}

.feature{top:435px;width:253px;height:71px;background:var(--accent);box-shadow:0 6px 6px -4px rgba(0,0,0,.25)}
.feature-icon{position:absolute;left:14px;top:14px;width:44px;height:44px;border-radius:50%;background:rgba(255,255,255,.35)}
.feature h3{position:absolute;left:67px;top:12px;font-size:16px;font-weight:400;color:var(--white)}
.feature p{position:absolute;left:68px;top:33px;width:180px;font-size:10.5px;line-height:15px;color:#eef5dc}

.welcome{left:208px;top:533px;width:530px}
.welcome h1{font-size:16px;font-weight:400;color:var(--heading);padding-bottom:4px;border-bottom:1px solid var(--rule)}
.welcome h1 span{color:var(--accent)}
.welcome p{font-size:10.5px;line-height:15px;margin-top:15px;color:var(--text)}
.read-more{display:inline-block;margin-top:15px;width:76px;height:22px;background:var(--accent);color:var(--white);font-size:10.5px;text-align:center;line-height:22px}
.divider{left:208px;top:697px;width:530px;height:1px;background:var(--rule)}

.thumb{top:709px;width:175px;height:143px;background:var(--white);padding:4px;box-shadow:0 6px 6px -4px rgba(0,0,0,.2)}
.thumb-photo{position:relative;width:100%;height:100%;background:linear-gradient(#5c78b0,#2f3c5e 55%,#5b4a2a 80%,#1b2030)}
.thumb-photo span{position:absolute;left:10px;bottom:12px;font-size:10px;color:var(--white)}
.story{top:865px;width:160px}
.story h4{font-size:11.5px;font-weight:400;color:var(--accent)}
.story p{margin-top:7px;font-size:10.5px;line-height:15px;color:var(--text)}

.side-links{left:760px;top:531px;width:243px;list-style:none}
.side-links li{height:29.5px;border-bottom:1px solid var(--rule);display:flex;align-items:center;justify-content:space-between;padding:0 2px 0 8px;font-size:13.5px;color:var(--accent)}

.map-title{left:761px;top:754px;font-size:14.5px;color:var(--accent)}
.map{left:761px;top:779px;width:242px;height:162px;background:var(--white);padding:4px;box-shadow:0 4px 5px -3px rgba(0,0,0,.25)}
.map-area{width:100%;height:100%;background:linear-gradient(160deg,#e2e2dc 0%,#ececea 45%,#a9c8f4 70%,#9fc3f3 100%)}

.site-footer{left:0;top:963px;width:1200px;height:37px;background:var(--footer);font-size:11px;color:#9ccf3c}
.footer-site{left:208px;top:14px}
.footer-follow{left:309px;top:13px;font-size:12px}
.social{top:11px;width:20px;height:20px;background:var(--white);border-radius:3px}
.copyright{left:796px;top:15px;width:207px;text-align:right;font-size:10.5px}
</style>
</head>
<body>

<header class="site-header abs">
  <div class="brand abs"><span class="brand-mark"></span>Velstrand</div>
  <div class="header-email abs">info@example.com</div>
  <nav class="main-nav abs">
    <a class="current" href="#" style="width:68px">Home</a>
    <a href="#" style="width:70px">About Us</a>
    <a href="#" style="width:68px">Data</a>
    <a href="#" style="width:73px">Events</a>
    <a href="#" style="width:73px">Blog</a>
    <a href="#" style="width:78px;margin-right:0">Contact Us</a>
  </nav>
</header>

<section class="slider abs">
  <div class="slide-photo" role="img" aria-label="Photo strip of the city: hills at dusk, downtown skyline by the river, waterfront at sunset"></div>
</section>
<div class="slide-arrow abs" style="left:225px;top:248px">
  <svg width="40" height="40" viewBox="0 0 40 40"><path d="M23 11 L14 20 L23 29" fill="none" stroke="#fff" stroke-width="4" stroke-linecap="round" stroke-linejoin="round"/></svg>
</div>
<div class="slide-arrow abs" style="left:942px;top:248px">
  <svg width="40" height="40" viewBox="0 0 40 40"><path d="M17 11 L26 20 L17 29" fill="none" stroke="#fff" stroke-width="4" stroke-linecap="round" stroke-linejoin="round"/></svg>
</div>
<div class="slide-dot abs" style="left:231px;top:391px"></div>
<div class="slide-dot abs" style="left:250px;top:391px"></div>
<div class="slide-dot abs" style="left:270px;top:391px"></div>
<div class="slide-dot abs" style="left:290px;top:391px"></div>

<article class="feature abs" style="left:208px">
  <div class="feature-icon" role="img" aria-label="Planning icon"></div>
  <h3>Planning</h3>
  <p>We strongly believe in being an honest and trustworthy</p>
</article>
<article class="feature abs" style="left:480px">
  <div class="feature-icon" role="img" aria-label="Development icon"></div>
  <h3>Development</h3>
  <p>We strongly believe in being an honest and trustworthy</p>
</article>
<article class="feature abs" style="left:750px">
  <div class="feature-icon" role="img" aria-label="Civic engagement icon"></div>
  <h3>Civic engagement</h3>
  <p>We strongly believe in being an honest and trustworthy</p>
</article>

<section class="welcome abs">
  <h1>Welcome To <span>Our Website</span></h1>
  <p>We strongly believe in being an honest and trustworthy business partner to each and every one of our clients. We are committed to always putting our clients' interests first. We are committed to always putting our clients' interests first.</p>
  <p>We strongly believe in being an honest and trustworthy business partner to each and every one of our clients. We are committed to always putting our clients' interests first. We are committed to always putting our clients' interests first.</p>
  <span class="read-more">read more</span>
</section>
<div class="divider abs"></div>

<div class="thumb abs" style="left:208px"><div class="thumb-photo" role="img" aria-label="Night skyline over the water"><span>Sample Text</span></div></div>
<div class="thumb abs" style="left:385px"><div class="thumb-photo" role="img" aria-label="Night skyline over the water"><span>Sample Text</span></div></div>
<div class="thumb abs" style="left:562px"><div class="thumb-photo" role="img" aria-label="Night skyline over the water"><span>Sample Text</span></div></div>

<div class="story abs" style="left:208px"><h4>sub heading</h4><p>We strongly believe in being an honest and trustworthy business partner to each and every</p></div>
<div class="story abs" style="left:388px"><h4>sub heading</h4><p>We strongly believe in being an honest and trustworthy business partner</p></div>
<div class="story abs" style="left:566px"><h4>sub heading</h4><p>We strongly believe in being an honest and trustworthy business partner to each and every one</p></div>

<ul class="side-links abs">
  <li>about the company<svg width="16" height="10" viewBox="0 0 16 10"><path d="M0 5H14M10 1L14 5L10 9" fill="none" stroke="#8db52c" stroke-width="1.8"/></svg></li>
  <li>company profile<svg width="16" height="10" viewBox="0 0 16 10"><path d="M0 5H14M10 1L14 5L10 9" fill="none" stroke="#8db52c" stroke-width="1.8"/></svg></li>
  <li>green templets for recycle<svg width="16" height="10" viewBox="0 0 16 10"><path d="M0 5H14M10 1L14 5L10 9" fill="none" stroke="#8db52c" stroke-width="1.8"/></svg></li>
  <li>about the company<svg width="16" height="10" viewBox="0 0 16 10"><path d="M0 5H14M10 1L14 5L10 9" fill="none" stroke="#8db52c" stroke-width="1.8"/></svg></li>
  <li>templets website<svg width="16" height="10" viewBox="0 0 16 10"><path d="M0 5H14M10 1L14 5L10 9" fill="none" stroke="#8db52c" stroke-width="1.8"/></svg></li>
</ul>

<div class="map-title abs">map location</div>
<div class="map abs"><div class="map-area" role="img" aria-label="Road map of the city centre by the bay"></div></div>

<footer class="site-footer abs">
  <span class="footer-site abs">velstrandplan.com &nbsp;|&nbsp;</span>
  <span class="footer-follow abs">Follow Us</span>
  <span class="social abs" style="left:369px" aria-label="Social link"></span>
  <span class="social abs" style="left:399px" aria-label="Social link"></span>
  <span class="social abs" style="left:429px" aria-label="Social link"></span>
  <span class="social abs" style="left:459px" aria-label="Feed link"></span>
  <span class="copyright abs">All Right Reserved 2013-14.</span>
</footer>

</body>
</html>
```